Fix Up Brochure for QVR Holdings

Hello,

We have an old structure and content of a brochure we previously sent to prospective/new clients. We would like to update it, make it more pleasant to the eye, and have some of the language cleaned up for a smooth read; more graphics on front and back.

You have the freedom to be creative with the graphic design... Not too edgy, but we do use unique option and hedging strategies that many firms do not. We are trying to convey that we are not your typical financial advisors.

Our business is QVR Holdings, which provides portfolio management to 20-80 year old individuals and small to medium businesses. (Our website is not create YET, but we are working on it right now).

This particular brochure will be given to new/prospective clients, making it a big marketing piece for our business. Attached is a photo of the folder which we have already created for the business, and this brochure (2 fold, not 3) will be inserted inside on thick paper. Therefore, the design of the brochure has to align with the photo attached.

Folder is about 9 x 12, so the brochure is standard 8 1/2 x 11, with about half inch margins. We would like 4 8 1/2 x 11 pages, or 2 17 x 11 landscape pages that we then fold.

All of the content inside the brochure (that we have right now) is also attached in PDF format. Please review/revise if needed.

Within the brochure, please feel free to include any images to do with the financial industry, as long as it's done tastefully.

Also, I have attached a jpeg of our logo. Colors are navy blue going into a royal blue, and lime green.

Conservative wise.. On a scale 1-10 (1 being most conservative) we are about a 6-7.
Updates

Uploaded PDF, a .eps version of the logo, QVR Holdings.

Also included color scheme for the blue & green in the logo

Industry/Entity Type

Financial

Requirements
Must have
• GREEN RGB:
R: 121
G: 199
B: 27

BLUE RGB:
R: 1
G: 19
B: 107

```html
<!DOCTYPE html>
<html lang="en">
<head>
<meta charset="utf-8">
<title>QVR Holdings — Brochure Cover</title>
<link rel="stylesheet" href="https://fonts.googleapis.com/css2?family=EB+Garamond:wght@400;600;700&display=swap">
<style>
  :root {
    --navy: #2e3192;
    --lime: #8dc63f;
    --white: #ffffff;
    --paper: #ffffff;
    --photo-light: #e4e4e2;
    --photo-mid: #c9cac8;
  }
  * { margin: 0; padding: 0; box-sizing: border-box; }
  html, body {
    width: 1200px; height: 902px; overflow: hidden;
    background: var(--paper);
    font-family: "EB Garamond", Georgia, serif;
  }
  .spread { position: relative; width: 1200px; height: 902px; }
  .spread-art { position: absolute; inset: 0; }

  .invite {
    position: absolute; left: 44px; top: 166px;
    width: 318px; padding-left: 8px;
    border-left: 5px solid var(--lime);
    color: var(--white); font-size: 12.4px; line-height: 15.6px;
    text-align: justify;
  }
  .invite ul { list-style: none; margin-top: 15.6px; text-align: left; }

  .brand {
    position: absolute; left: 990px; top: 140px; width: 175px;
    display: flex; flex-direction: column; align-items: center; gap: 10px;
  }
  .brand-mark { width: 34px; height: 34px; background: var(--navy); border-radius: 50%; }
  .brand-name {
    color: var(--navy); font-size: 16px; font-weight: 600;
    letter-spacing: 3px; text-transform: uppercase; white-space: nowrap;
  }

  .contact {
    position: absolute; right: 634px; top: 737px;
    text-align: right; font-size: 10.2px; line-height: 14px; color: var(--white);
    font-style: normal;
  }
  .contact .label { color: var(--lime); font-weight: 700; margin-right: 6px; }
  .contact .accent { color: var(--lime); }

  .headline {
    position: absolute; left: 650px; top: 734px;
    color: var(--white); font-size: 24.5px; font-weight: 700; line-height: 31px;
    letter-spacing: 0.2px;
  }
</style>
</head>
<body>
<main class="spread">
  <svg class="spread-art" width="1200" height="902" viewBox="0 0 1200 902">
    <defs>
      <linearGradient id="photoTone" x1="0" y1="0" x2="1" y2="1">
        <stop offset="0" stop-color="#d6d7d5"/>
        <stop offset="0.55" stop-color="#e4e4e2"/>
        <stop offset="1" stop-color="#c9cac8"/>
      </linearGradient>
      <linearGradient id="headerTone" x1="0" y1="0" x2="1" y2="1">
        <stop offset="0" stop-color="#ffffff"/>
        <stop offset="1" stop-color="#ededf0"/>
      </linearGradient>
      <clipPath id="frameClip">
        <path d="M938,60 C932,165 870,210 775,248 C680,288 612,370 606,610 C700,680 1000,690 1200,610 L1200,60 Z"/>
      </clipPath>
    </defs>

    <!-- navy base -->
    <rect x="0" y="60" width="1200" height="776" fill="var(--navy)"/>

    <!-- lime edge along the frame curve -->
    <path d="M918,60 C915,160 850,200 760,235 C660,275 600,360 598,612 C700,680 1000,690 1200,610 L1200,60 Z" fill="var(--lime)"/>

    <!-- lower right lime swoosh and rule -->
    <path d="M1200,570 C1120,650 980,690 780,686 C1000,700 1130,690 1200,670 Z" fill="var(--lime)"/>
    <path d="M1200,592 C1130,652 990,684 800,686" fill="none" stroke="var(--white)" stroke-width="2"/>

    <!-- framed panel: header and photo -->
    <g clip-path="url(#frameClip)">
      <rect x="590" y="60" width="610" height="212" fill="url(#headerTone)"/>
      <rect x="590" y="272" width="610" height="6" fill="var(--lime)"/>
      <rect x="590" y="278" width="610" height="430" fill="url(#photoTone)" role="img" aria-label="Photograph: two business colleagues fitting together large white jigsaw puzzle pieces on a grey floor"/>
    </g>

    <!-- lower left lime swoosh -->
    <path d="M0,580 C90,640 260,672 430,676 C250,688 100,688 0,672 Z" fill="var(--lime)"/>
    <path d="M0,592 C100,645 260,672 430,676" fill="none" stroke="var(--white)" stroke-width="2"/>

    <!-- white sweep across the fold -->
    <path d="M0,702 C250,700 520,690 600,625 C680,690 950,712 1200,716" fill="none" stroke="var(--white)" stroke-width="2"/>
  </svg>

  <section class="invite">
    <p>We invite you to contact us. We will help you define your specific goals and a plan toward achieving them. Call today to begin putting QVR Holdings to work for you and your family, or visit www.qvrholdings-demo.com for detailed information about:</p>
    <ul>
      <li>- Investment Management</li>
      <li>- Our Investment Philosophy</li>
      <li>- The QVR Holdings team</li>
    </ul>
  </section>

  <div class="brand">
    <span class="brand-mark"></span>
    <span class="brand-name">QVR Holdings</span>
  </div>

  <address class="contact">
    <div><span class="label">Main Office:</span>4470 Lakeview Terrace, Suite 210</div>
    <div>Springfield, IL 62704</div>
    <div class="accent">p: 555 - 302 - 0148</div>
    <div class="accent">info@qvrholdings-demo.com</div>
    <div class="accent">www.qvrholdings-demo.com</div>
  </address>

  <h1 class="headline">Customized Strategies<br>to Meet Your Financial Goals</h1>
</main>
</body>
</html>
```